Website needed for Entertainment Company [Wordpress & Mobile Site] (Contest)

"Tumble Scholars" does Acrobatic Educational Shows for schools.
We need a 4-Page Wordpress site, for BOTH Desktop & Mobile
THINGS WE'D LIKE ON THE HOME PAGE
- Book Now buttons
- Panel advertising "Kindness-Shield Tumbling Tour" with subheading "Educating the Victim, Empowering the Bystander, and Enlightening the Bully" with Photo & 'Read More'
- text somewhere saying "Tumble Scholars engages children in important topics, by utilising Parkour & Acrobatics to captivate and enthrall todays youngest generation."
- Panel advertising Teachers Resources: "Curriculum based resources for teachers including lesson plans, workbooks, and physical activities for before & after the show." Maybe even some boxes that say a subject that is covered (eg. Mathematics. Science. PD/H/PE.)
- Everything else that you recommend
4 PAGES:
- Home Page
- About Us
- Our Program & Shows
- Teachers Resources Portal
NOTE: Transparent & Source files for logo will be provided soon (recently finished being designed)

```html
<!DOCTYPE html>
<html lang="en">
<head>
<meta charset="utf-8">
<title>Tumble Scholars – Home</title>
<link href="https://fonts.googleapis.com/css2?family=Raleway:ital,wght@0,400;0,600;0,700;0,800;1,700&family=Open+Sans:wght@400;600;700&display=swap" rel="stylesheet">
<style>
:root{
  --orange:#f26b22;
  --green:#3aa845;
  --blue:#1e8fd6;
  --dark:#232323;
  --darker:#1a1a1a;
  --mid:#2e2e2e;
  --light:#f1f1f1;
  --text:#bdbdbd;
  --ink:#333;
  --white:#fff;
}
*{box-sizing:border-box;margin:0;padding:0}
html,body{width:1200px;height:3972px;overflow:hidden}
body{font-family:"Open Sans",sans-serif;color:var(--ink);background:var(--dark);position:relative}
h1,h2,h3,h4{font-family:"Raleway",sans-serif}
section,header,footer{position:absolute;left:0;width:1200px}
.abs{position:absolute}

/* header */
.site-header{top:0;height:168px;background:var(--white)}
.brand{left:24px;top:28px;display:flex;align-items:center;gap:10px}
.brand-dot{width:22px;height:22px;border-radius:50%;background:var(--orange)}
.brand-name{font-family:"Raleway",sans-serif;font-weight:800;font-size:28px;color:var(--orange)}
.topinfo{top:40px;font-size:11px;color:#777;line-height:16px}
.topinfo b{color:var(--green);font-size:13px}
.socials{left:1030px;top:44px;display:flex;gap:10px}
.socials span{width:18px;height:18px;border-radius:50%;background:#ddd;display:block}
.socials span:first-child{background:var(--orange)}
.mainnav{top:120px;left:0;width:1200px;height:48px;background:#f5f5f5;border-top:1px solid #e3e3e3}
.mainnav ul{list-style:none;display:flex;gap:38px;position:absolute;left:80px;top:15px}
.mainnav li{font-size:13px;font-weight:600;color:#444}
.mainnav li.active{color:var(--ink);border-bottom:3px solid var(--orange);padding-bottom:11px}
.btn-book{left:960px;top:6px;width:150px;height:36px;background:var(--orange);color:var(--white);font-weight:700;font-size:13px;display:flex;align-items:center;justify-content:center}

/* hero */
.hero{top:168px;height:512px;background:var(--light);overflow:hidden}
.hero-media{left:520px;top:0;width:680px;height:512px;background:linear-gradient(120deg,#e9eaec 0%,#d9dde0 45%,#3aa8b8 60%,#2c2c2c 75%,#cfd3d6 90%)}
.hero-title{left:88px;top:232px;font-size:40px;font-weight:700;color:#2a2a2a;width:640px;line-height:48px}
.hero-text{left:88px;top:290px;width:420px;font-size:12px;line-height:19px;color:#666}
.hero-btns{left:88px;top:350px;display:flex;gap:16px}
.hero-btns span{width:130px;height:38px;display:flex;align-items:center;justify-content:center;font-size:12px;font-weight:700}
.b-blue{background:var(--blue);color:var(--white)}
.b-line{border:1px solid #444;color:#333}

/* feature cards */
.features{top:680px;height:480px;background:var(--mid)}
.fcard{top:52px;width:320px;height:368px}
.fcard .media{height:280px}
.fcard .label{height:88px;display:flex;flex-direction:column;align-items:center;justify-content:center;color:var(--white)}
.fcard h3{font-size:28px;font-weight:700}
.fcard .label i{display:block;width:40px;height:2px;background:rgba(255,255,255,.7);margin-top:8px}

/* about */
.about{top:1160px;height:480px;background:var(--darker)}
.about-media{left:600px;top:0;width:600px;height:480px;background:radial-gradient(ellipse at 55% 45%,#5a5a5a 0%,#333 45%,#1e1e1e 100%)}
.about-copy{left:88px;top:36px;width:460px}
.eyebrow{color:var(--orange);font-size:12px;font-weight:600}
.about-copy h2{color:var(--white);font-size:20px;font-weight:700;margin-top:4px}
.rule{width:40px;height:2px;background:var(--orange);margin:14px 0 20px}
.about-copy p{font-size:11.5px;line-height:19px;color:var(--text);margin-bottom:16px}
.readmore{color:var(--green);font-size:11px;font-weight:700}

/* team */
.team{top:1640px;height:620px;background:#2a2a2a;overflow:hidden}
.team-ghost{left:340px;top:150px;font-family:"Raleway",sans-serif;font-weight:800;font-size:130px;letter-spacing:14px;color:rgba(255,255,255,.05)}
.sec-title{width:1200px;text-align:center;color:var(--white);font-size:20px;font-weight:600}
.sec-title i{display:block;width:40px;height:2px;background:var(--green);margin:10px auto 0}
.member{top:160px;width:240px;height:360px}

/* testimonials */
.clients{top:2260px;height:380px;background:linear-gradient(90deg,#1b1b1b 0%,#2b2b2b 50%,#1b1b1b 100%)}
.clients h2{left:88px;top:48px;color:var(--white);font-size:18px;font-weight:700}
.clients .rule{position:absolute;left:88px;top:76px;margin:0}
.quote{top:108px;width:320px}
.quote p{font-size:11.5px;line-height:18px;color:var(--text)}
.who{display:flex;gap:12px;align-items:center;margin-top:20px}
.who .av{width:40px;height:40px;border-radius:50%;background:#6a6a6a}
.who b{display:block;color:var(--white);font-size:11px;letter-spacing:.5px}
.who small{color:#999;font-size:10px}
.dots{left:88px;top:318px;display:flex;gap:6px}
.dots span{width:8px;height:8px;border-radius:50%;background:#666}
.dots span:first-child{background:var(--orange)}

/* mission band */
.mission{top:2640px;height:240px;background:var(--orange);display:flex;align-items:center;justify-content:center}
.mission p{width:700px;text-align:center;font-family:"Raleway",sans-serif;font-style:italic;font-weight:700;font-size:21px;line-height:30px;color:var(--white)}

/* news */
.news{top:2880px;height:820px;background:#303030}
.news h2{top:60px;font-size:38px;font-weight:400;color:var(--white);width:1200px;text-align:center}
.news .rule{position:absolute;left:580px;top:118px;margin:0;background:var(--green)}
.ncard{top:160px;width:320px;height:500px;background:var(--white)}
.ncard .media{height:230px;position:relative}
.date{position:absolute;left:20px;bottom:-26px;width:56px;height:56px;border-radius:50%;color:var(--white);display:flex;flex-direction:column;align-items:center;justify-content:center;font-weight:700;font-size:18px;line-height:18px}
.date small{font-size:9px;font-weight:600}
.ncard .body{padding:44px 22px 0}
.ncard h3{color:var(--green);font-size:22px;font-weight:600}
.ncard p{font-size:11.5px;line-height:18px;color:#777;margin-top:12px}
.meta{position:absolute;left:22px;right:22px;bottom:18px;border-top:1px solid #e5e5e5;padding-top:12px;font-size:10px;color:#999;display:flex;justify-content:space-between}
.viewmore{left:540px;top:716px;width:120px;height:34px;border:1px solid #777;border-radius:18px;color:#aaa;font-size:11px;font-weight:600;display:flex;align-items:center;justify-content:center}

/* footer */
.site-footer{top:3700px;height:272px;background:var(--darker)}
.fcol{top:40px;width:240px}
.fcol h4{display:flex;align-items:center;gap:10px;color:var(--orange);font-size:16px;font-weight:600}
.fcol p{color:#999;font-size:11px;line-height:18px;margin:12px 0 0 30px}
.fsocial{display:flex;gap:8px;margin:12px 0 0 30px}
.fsocial span{width:22px;height:22px;border-radius:50%;background:var(--blue)}
.fsocial span:first-child{background:var(--orange)}
.bottom{top:200px;width:1200px;text-align:center}
.bottom .links{font-size:10px;font-weight:600;color:#aaa;letter-spacing:.5px;word-spacing:10px}
.bottom .copy{font-size:10px;color:#777;margin-top:10px}
</style>
</head>
<body>

<header class="site-header">
  <div class="abs brand"><span class="brand-dot"></span><span class="brand-name">Tumble Scholars</span></div>
  <div class="abs topinfo" style="left:480px">We tour schools across the region<br><b>Book a visit today</b></div>
  <div class="abs topinfo" style="left:820px">Give us a call<br><b>1300 555 0142</b></div>
  <div class="abs socials"><span></span><span></span><span></span></div>
  <nav class="abs mainnav">
    <ul>
      <li class="active">HOME</li><li>About Us</li><li>Our Program &amp; Shows</li><li>Teachers Resources Portal</li><li>Contact</li>
    </ul>
    <div class="abs btn-book">BOOK NOW</div>
  </nav>
</header>

<section class="hero">
  <div class="abs hero-media" role="img" aria-label="Performer posing in a teal aerial silk against a bright studio wall"></div>
  <h1 class="abs hero-title">Kindness-Shield Tumbling Tour</h1>
  <p class="abs hero-text">Educating the victim, empowering the bystander and enlightening the bully through an acrobatic live show built for school halls.</p>
  <div class="abs hero-btns"><span class="b-blue">BOOK NOW</span><span class="b-line">READ MORE</span></div>
</section>

<section class="features">
  <div class="abs fcard" style="left:88px">
    <div class="media" role="img" aria-label="Acrobats performing on a school stage" style="background:linear-gradient(135deg,#8a4a2a,#c0392b 50%,#3a2a20)"></div>
    <div class="label" style="background:var(--orange)"><h3>School Shows</h3><i></i></div>
  </div>
  <div class="abs fcard" style="left:440px">
    <div class="media" role="img" aria-label="Dancer leaping in a workshop" style="background:linear-gradient(135deg,#2a2f3a,#8a3a4a 55%,#1c1f26)"></div>
    <div class="label" style="background:var(--green)"><h3>Workshops</h3><i></i></div>
  </div>
  <div class="abs fcard" style="left:792px">
    <div class="media" role="img" aria-label="Students exercising in a classroom gym" style="background:linear-gradient(135deg,#d8c9a0,#b7a47a 50%,#7a8a99)"></div>
    <div class="label" style="background:var(--blue)"><h3>Curriculum</h3><i></i></div>
  </div>
</section>

<section class="about">
  <div class="abs about-media" role="img" aria-label="Silhouette of a dancer mid-leap on a dark stage"></div>
  <div class="abs about-copy">
    <div class="eyebrow">Who we are</div>
    <h2>TUMBLE SCHOLARS</h2>
    <div class="rule"></div>
    <p>Tumble Scholars engages children in important topics by utilising parkour and acrobatics to captivate and enthral today's youngest generation. Our touring team brings a full live show into the school hall, with lighting, music and a story that every student can follow from start to finish.</p>
    <p>Every performance is backed by curriculum based resources for teachers, including lesson plans, workbooks and physical activities for before and after the show, so the message keeps working long after the final bow and the crew has packed up for the day.</p>
    <p>Our performers are trained coaches and educators who care about safety, inclusion and kindness.</p>
    <div class="readmore">READ MORE</div>
  </div>
</section>

<section class="team">
  <div class="abs team-ghost">SCHOLARS</div>
  <h2 class="abs sec-title" style="top:72px">OUR TEAM<i></i></h2>
  <div class="abs member" style="left:96px;background:linear-gradient(160deg,#2f8fd8,#1a5f99)" role="img" aria-label="Team member portrait"></div>
  <div class="abs member" style="left:352px;background:linear-gradient(160deg,#d7d7d7,#9a9a9a)" role="img" aria-label="Team member portrait"></div>
  <div class="abs member" style="left:608px;background:linear-gradient(160deg,#cfcfcf,#8d8d8d)" role="img" aria-label="Team member portrait"></div>
  <div class="abs member" style="left:864px;background:linear-gradient(160deg,#e2dcd6,#a79b90)" role="img" aria-label="Team member portrait"></div>
</section>

<section class="clients">
  <h2 class="abs">OUR CLIENT SAY</h2>
  <div class="rule"></div>
  <div class="abs quote" style="left:88px">
    <p>The whole school was talking about the show for weeks. Students finally had words for what they saw in the playground and the teachers loved the follow-up lessons.</p>
    <div class="who"><span class="av"></span><div><b>MAREN HOLT</b><small>Principal</small></div></div>
  </div>
  <div class="abs quote" style="left:440px">
    <p>Energetic, safe and genuinely moving. Our bystander lesson the next morning was the best discussion my class has had all year. We will book again.</p>
    <div class="who"><span class="av"></span><div><b>PRIYA DALTON</b><small>Teacher</small></div></div>
  </div>
  <div class="abs quote" style="left:792px">
    <p>Professional from the first call to the final bow. The workbooks fit straight into our wellbeing program and the kids were asking for more.</p>
    <div class="who"><span class="av"></span><div><b>LEAH CORRIGAN</b><small>Coordinator</small></div></div>
  </div>
  <div class="abs dots"><span></span><span></span><span></span></div>
</section>

<section class="mission">
  <p>Tumble Scholars engages children in important topics, by utilising Parkour &amp; Acrobatics to captivate and enthrall todays youngest generation.</p>
</section>

<section class="news">
  <h2 class="abs">Latest News</h2>
  <div class="rule"></div>
  <article class="abs ncard" style="left:88px">
    <div class="media" role="img" aria-label="Gymnast stretching in a studio" style="background:linear-gradient(135deg,#e6e1da,#b89c8a)"><div class="date" style="background:var(--green)">29<small>APR</small></div></div>
    <div class="body"><h3>Vestibulum Ante Ipsum</h3><p>Spring tour dates are now open for booking across primary schools, with new workshop add-ons for senior classes.</p></div>
    <div class="meta"><span>Admin</span><span>News</span><span>4</span></div>
  </article>
  <article class="abs ncard" style="left:440px">
    <div class="media" role="img" aria-label="Dancer performing on a dark stage" style="background:linear-gradient(135deg,#3a3a3a,#9a6a5a 55%,#222)"><div class="date" style="background:var(--green)">17<small>MAR</small></div></div>
    <div class="body"><h3>Donec Eget Tellus</h3><p>Meet the newest members of our touring crew and find out what they bring to the kindness program this season.</p></div>
    <div class="meta"><span>Admin</span><span>Announcements</span><span>2</span></div>
  </article>
  <article class="abs ncard" style="left:792px">
    <div class="media" role="img" aria-label="Group of children in an outdoor fitness class" style="background:linear-gradient(135deg,#d9c7a5,#7fa06a 55%,#5a7a8a)"><div class="date" style="background:var(--green)">15<small>FEB</small></div></div>
    <div class="body"><h3>Nulla Venenatis</h3><p>New teacher resources are live in the portal, including workbooks for mathematics, science and PD/H/PE.</p></div>
    <div class="meta"><span>Admin</span><span>News</span><span>6</span></div>
  </article>
  <div class="abs viewmore">VIEW MORE</div>
</section>

<footer class="site-footer">
  <div class="abs fcol" style="left:88px">
    <h4><svg width="20" height="20" viewBox="0 0 24 24"><path d="M12 2a7 7 0 0 0-7 7c0 5 7 13 7 13s7-8 7-13a7 7 0 0 0-7-7zm0 9.5A2.5 2.5 0 1 1 12 6a2.5 2.5 0 0 1 0 5.5z" fill="var(--orange)"/></svg>Location</h4>
    <p>Studio 4, Harbour Lane<br>Northgate District</p>
  </div>
  <div class="abs fcol" style="left:360px">
    <h4><svg width="20" height="20" viewBox="0 0 24 24"><circle cx="12" cy="12" r="9" fill="none" stroke="var(--orange)" stroke-width="2"/><path d="M12 7v5l3 2" stroke="var(--orange)" stroke-width="2" fill="none"/></svg>Opening Hours</h4>
    <p>Mon – Fri: 8am – 5pm<br>Sat: 9am – 1pm</p>
  </div>
  <div class="abs fcol" style="left:630px">
    <h4><svg width="20" height="20" viewBox="0 0 24 24"><path d="M6.6 10.8a15 15 0 0 0 6.6 6.6l2.2-2.2a1 1 0 0 1 1-.25 11 11 0 0 0 3.6.6 1 1 0 0 1 1 1V20a1 1 0 0 1-1 1A17 17 0 0 1 3 4a1 1 0 0 1 1-1h3.5a1 1 0 0 1 1 1c0 1.25.2 2.45.6 3.6a1 1 0 0 1-.25 1z" fill="var(--orange)"/></svg>Contact Us</h4>
    <p>1300 555 0142<br>hello@tumblescholars.example</p>
  </div>
  <div class="abs fcol" style="left:900px">
    <h4><svg width="20" height="20" viewBox="0 0 24 24"><circle cx="6" cy="12" r="3" fill="var(--orange)"/><circle cx="18" cy="6" r="3" fill="var(--orange)"/><circle cx="18" cy="18" r="3" fill="var(--orange)"/><path d="M6 12 18 6M6 12l12 6" stroke="var(--orange)" stroke-width="2"/></svg>Stay Connected</h4>
    <div class="fsocial"><span></span><span></span><span></span><span></span></div>
  </div>
  <div class="abs bottom">
    <div class="links">ABOUT PHILOSOPHY OUR STAFF FAQ WORKSHOPS TUITION CURRICULUM UPCOMING SHOWS CONTACT</div>
    <div class="copy">Copyright © Tumble Scholars. All Rights Reserved.</div>
  </div>
</footer>

</body>
</html>
```